Shopify store for hemp

I need a store designed for Shopify for my hemp company. I currently have a brick and mortar store, but we are looking to get some business online as well. I will upload our logo for reference. We want a clean look. Categories like THCA Flower, Concentrates, Vapes, Edibles would be nice so that we can put individual products under them. I want something about all products being third-party lab tested. All products are sourced in the United States.
Updates

Need extra days to review

Target Market(s)

Former customers who live in different areas and signed up for our marketing list.

Industry/Entity Type

Hemp/Cannabis

Coding

Coded - Design and coding required

Number of Pages Required

1 page

Requirements
Must have
• Clean feel

```html
<!DOCTYPE html>
<html lang="en">
<head>
<meta charset="utf-8">
<title>Ridgeline Hemp — Online Store</title>
<link href="https://fonts.googleapis.com/css2?family=Jost:wght@300;400;500;600;700&display=swap" rel="stylesheet">
<style>
:root{
  --green:#2e9e22;
  --green-dark:#1f7a16;
  --ink:#1b1b1b;
  --text:#555;
  --muted:#8a8a8a;
  --line:#e6e6e6;
  --soft:#f2f2f2;
  --white:#fff;
  --topbar:#161616;
}
*{box-sizing:border-box;margin:0;padding:0}
html,body{width:1200px;height:5072px;overflow:hidden}
body{font-family:"Jost",sans-serif;color:var(--ink);background:var(--white);position:relative}
.abs{position:absolute}
a{color:inherit;text-decoration:none}
.btn{display:inline-flex;align-items:center;justify-content:center;border-radius:20px;font-size:8px;font-weight:600;text-transform:uppercase;letter-spacing:.3px;height:30px}
.btn-green{background:var(--green);color:#fff}
.btn-white{background:#fff;color:var(--ink)}
.btn-outline{border:1px solid var(--green);color:var(--green);background:#fff}
.ph{border-radius:6px}
/* top bar */
.topbar{top:0;left:0;width:1200px;height:30px;background:var(--topbar);color:#fff;font-size:9px;display:flex;align-items:center;justify-content:center;letter-spacing:.2px}
/* header */
.header{top:30px;left:0;width:1200px;height:82px;display:flex;align-items:center;padding:0 90px}
.nav{display:flex;gap:15px;font-size:10px;font-weight:500}
.brand{position:absolute;left:540px;top:10px;display:flex;align-items:center;gap:8px}
.brand-mark{width:44px;height:44px;border-radius:50%;background:var(--green)}
.brand-name{font-size:13px;font-weight:600;color:var(--green);line-height:1.1;width:60px}
.perks{position:absolute;right:90px;top:24px;display:flex;gap:36px}
.perk{display:flex;align-items:center;gap:9px}
.perk small{display:block;font-size:7px;color:var(--muted)}
.perk b{display:block;font-size:10px;font-weight:500}
/* hero */
.hero{top:112px;left:0;width:1200px;height:552px;background:radial-gradient(ellipse at 28% 45%,#3c3f3d 0%,#2d3a3f 35%,#3f5662 70%,#4a6470 100%)}
.hero-copy{position:absolute;right:90px;top:190px;text-align:right;color:#fff}
.hero-copy h1{font-size:31px;font-weight:500;line-height:1.4}
.hero-copy p{font-size:9px;margin-top:10px}
.hero-btns{display:flex;gap:14px;justify-content:flex-end;margin-top:22px}
.dots{position:absolute;left:572px;top:528px;display:flex;gap:6px}
.dots i{width:22px;height:3px;background:rgba(255,255,255,.5);display:block}
.dots i:first-child{background:#fff}
/* why */
.why-img{top:738px;left:114px;width:483px;height:399px;border-radius:10px;background:linear-gradient(135deg,#6b5a4a,#b9a58c 45%,#7d3b30 80%,#5b2c24)}
.why{top:810px;left:635px;width:450px}
.why h2{font-size:19px;font-weight:500}
.why p{font-size:10px;color:var(--text);line-height:1.6;margin-top:16px}
.why h4{font-size:9px;font-weight:600;margin-top:18px}
.commit{display:flex;gap:30px;margin-top:12px}
.commit div{text-align:center;font-size:7px;color:var(--text)}
.commit svg{display:block;margin:0 auto 6px}
.why .btns{display:flex;gap:12px;margin-top:22px}
/* featured */
.band-grey{background:var(--soft);left:0;width:1200px}
.sec-title{position:absolute;left:0;width:1200px;text-align:center}
.sec-title h2{font-size:19px;font-weight:500}
.sec-title p{font-size:8px;color:var(--muted);margin-top:8px}
.tabs{position:absolute;top:1317px;left:396px;width:408px;height:26px;border:1px solid #d8d8d8;border-radius:14px;display:flex;align-items:center;padding:3px;font-size:9px}
.tabs span{padding:4px 22px;border-radius:10px}
.tabs .on{background:var(--green);color:#fff}
.card{position:absolute;width:237px;background:#fff;border:1px solid var(--line);border-radius:4px;text-align:center}
.card .shot{position:absolute;left:10px;top:10px;width:215px;height:270px;border-radius:3px}
.card .off{position:absolute;left:16px;top:16px;background:#b8e986;color:var(--ink);font-size:7px;font-weight:600;padding:2px 7px;border-radius:9px}
.stars{color:#d0d0d0;font-size:9px;letter-spacing:1px}
.stars em{font-style:normal;font-size:7px;color:var(--muted);margin-left:4px}
.card h3{font-size:14px;font-weight:600;margin-top:6px}
.price{font-size:11px;margin-top:6px;color:var(--ink)}
.price s{color:#e07070;margin-left:6px}
.card .meta{position:absolute;left:0;width:100%}
/* promos */
.promo{top:1911px;width:498px;height:299px;border-radius:6px;background:linear-gradient(90deg,#f3f3f3,#e2e2e2)}
.promo .txt{position:absolute;left:40px;top:92px}
.promo .txt small{font-size:14px;display:block}
.promo .txt b{font-size:22px;font-weight:600;display:block;line-height:1.2}
.promo .txt p{font-size:7px;color:var(--muted);margin-top:6px}
.promo .txt .btn{margin-top:18px;height:26px;width:100px}
.promo .art{position:absolute;border-radius:8px}
/* countdown */
.count{position:absolute;left:10px;top:244px;width:215px;display:flex;justify-content:space-between;align-items:center;padding:0 6px}
.count span{width:40px;height:30px;background:#fff;border-radius:3px;font-size:11px;font-weight:500;display:flex;align-items:center;justify-content:center;box-shadow:0 1px 3px rgba(0,0,0,.1)}
.count i{font-style:normal;font-size:11px}
/* benefits */
.benefit{position:absolute;width:330px;display:flex;gap:14px}
.benefit .ic{flex:none;width:68px;height:68px;border-radius:50%;background:var(--green);display:flex;align-items:center;justify-content:center}
.benefit h4{font-size:9px;font-weight:600;margin-top:12px}
.benefit p{font-size:8px;color:var(--text);line-height:1.6;margin-top:6px}
.video{top:2857px;left:778px;width:330px;height:285px;background:linear-gradient(160deg,#2f4a3a,#1d2f26 55%,#3c5a6e)}
.play{position:absolute;left:136px;top:113px;width:58px;height:58px;border-radius:50%;border:2px solid rgba(255,255,255,.7)}
/* shipping */
.ship-band{top:3388px;height:170px}
.van{top:3240px;left:414px;width:300px;height:300px;border-radius:20px;background:radial-gradient(ellipse at 50% 60%,#9a9a9a,#555 55%,rgba(240,240,240,0) 72%)}
.svc{position:absolute;width:230px;text-align:center}
.svc h4{font-size:10px;font-weight:600;display:flex;justify-content:center;gap:8px;align-items:center}
.svc p{font-size:8px;color:var(--text);line-height:1.55;margin-top:8px}
/* news */
.news-main{top:3723px;left:91px;width:498px;height:345px;background:linear-gradient(135deg,#4c6b3a,#2c4422 45%,#b68c6c 62%,#3a5430)}
.news-body{top:4082px;left:91px;width:498px}
.date{font-size:8px;color:var(--muted)}
.news-body h3,.news-item h3{font-size:9px;font-weight:600;text-transform:uppercase;margin-top:10px}
.news-body p,.news-item p{font-size:8px;color:var(--text);line-height:1.65;margin-top:10px}
.more{font-size:8px;font-weight:600;margin-top:10px;display:block}
.news-item{position:absolute;left:609px;width:490px;height:150px}
.news-item .thumb{position:absolute;left:0;top:0;width:152px;height:150px;border-radius:8px}
.news-item .body{position:absolute;left:173px;top:0;width:300px}
.scroll{top:3723px;left:1100px;width:3px;height:500px;background:#ececec}
.scroll i{display:block;width:3px;height:220px;background:#b9b9b9;margin-top:200px}
/* reviews */
.review{position:absolute;top:4442px;width:328px;height:237px;background:#fff;border-radius:8px;box-shadow:0 2px 10px rgba(0,0,0,.07)}
.review .avatar{position:absolute;left:78px;top:24px;width:90px;height:98px;border-radius:6px}
.review .who{position:absolute;left:180px;top:50px}
.review .who b{font-size:10px;font-weight:600;display:block}
.review .who small{font-size:8px;color:var(--muted);display:block;margin-top:6px}
.review .who .st{color:var(--green);font-size:10px;letter-spacing:1px;margin-top:6px;display:block}
.review .q{position:absolute;left:24px;top:150px;font-size:22px;color:#bbb;line-height:1}
.review p{position:absolute;left:24px;top:170px;width:284px;font-size:8px;color:var(--text);line-height:1.6}
/* footer */
.foot-brand{top:4770px;left:88px;display:flex;align-items:center;gap:10px}
.foot-brand .brand-mark{width:84px;height:84px}
.foot-contact{top:4880px;left:91px;font-size:8px;line-height:1;color:var(--ink)}
.foot-contact div{display:flex;align-items:center;gap:8px;margin-bottom:13px}
.fcol{position:absolute;top:4847px}
.fcol h4{font-size:11px;font-weight:500;margin-bottom:12px}
.fcol a{display:block;font-size:8px;margin-bottom:13px}
.news-form{display:flex;gap:6px;margin-top:4px}
.news-form span{width:170px;height:22px;border-bottom:1px solid var(--line);font-size:8px;color:var(--muted);display:flex;align-items:center;padding-left:14px}
.news-form b{height:20px;width:62px;background:#2a2a2a;color:#fff;font-size:7px;font-weight:500;border-radius:10px;display:flex;align-items:center;justify-content:center}
.social{display:flex;gap:12px;margin-top:12px}
.social i{width:10px;height:10px;border-radius:50%;border:1px solid #999;display:block}
.copy{top:5038px;left:91px;font-size:8px}
.pay{top:5033px;left:970px;display:flex;gap:6px}
.pay i{display:block;width:22px;height:14px;border-radius:2px;background:#d8dde6}
</style>
</head>
<body>

<div class="abs topbar">WARNING: For existing adult smokers and vapers only. Minimum age as stipulated by local laws.</div>

<header class="abs header">
  <nav class="nav">
    <a>Home</a><a>Vape Shop</a><a>THCA Flower</a><a>Concentrates</a><a>Edibles</a><a>Blog</a><a>Contact Us</a>
  </nav>
  <div class="brand"><span class="brand-mark"></span><span class="brand-name">Ridgeline Hemp</span></div>
  <div class="perks">
    <div class="perk"><svg width="22" height="22" viewBox="0 0 22 22" fill="none" stroke="#2e9e22" stroke-width="1.4"><circle cx="11" cy="11" r="8"/><path d="M7 11l3 3 5-6"/></svg><div><small>Certified</small><b>Medical Standard</b></div></div>
    <div class="perk"><svg width="22" height="22" viewBox="0 0 22 22" fill="none" stroke="#2e9e22" stroke-width="1.4"><path d="M11 3c4 4 4 10 0 16c-4-6-4-12 0-16z"/><path d="M11 8v11"/></svg><div><small>Organic</small><b>100% Organic Store</b></div></div>
    <div class="perk"><svg width="24" height="22" viewBox="0 0 24 22" fill="none" stroke="#2e9e22" stroke-width="1.4"><rect x="2" y="5" width="13" height="10"/><path d="M15 8h4l3 4v3h-7"/><circle cx="6" cy="17" r="2"/><circle cx="18" cy="17" r="2"/></svg><div><small>Free Shipping</small><b>Orders over $99</b></div></div>
  </div>
</header>

<section class="abs hero" role="img" aria-label="Two cannabis oil dropper bottles on a dark tray with hemp leaves">
  <div class="hero-copy">
    <h1>Harnessing The Potential Of<br>Cannabis Oil For Wellness</h1>
    <p>Empowering Wellness with the Healing Properties of Cannabis Oil</p>
    <div class="hero-btns">
      <span class="btn btn-white" style="width:98px">Shop Now</span>
      <span class="btn btn-white" style="width:142px;color:var(--green);justify-content:space-between;padding:0 4px 0 26px">Learn More
        <svg width="22" height="22" viewBox="0 0 22 22"><circle cx="11" cy="11" r="11" fill="#2e9e22"/><path d="M7 11h8M12 8l3 3-3 3" stroke="#fff" stroke-width="1.5" fill="none"/></svg></span>
    </div>
  </div>
  <div class="dots"><i></i><i></i><i></i></div>
</section>

<div class="abs why-img" role="img" aria-label="Storefront window of the hemp shop with a snowman display and free samples sign"></div>
<section class="abs why">
  <h2>Why Choose Us ?</h2>
  <p>Every product we carry is third-party lab tested and sourced in the United States. Our shop started as a local storefront, and we bring the same care, honest labels and friendly advice to every order we ship online.</p>
  <h4>Our commitment:</h4>
  <div class="commit">
    <div><svg width="34" height="34" viewBox="0 0 34 34" fill="none" stroke="#333" stroke-width="1.3"><path d="M5 24c6 0 8-2 12-2h8l4-3"/><path d="M17 17c-4-3-4-8 0-11c4 3 4 8 0 11z"/></svg>Natural</div>
    <div><svg width="34" height="34" viewBox="0 0 34 34" fill="none" stroke="#333" stroke-width="1.3"><circle cx="17" cy="17" r="13"/><path d="M8 8l18 18"/><path d="M17 10c4 3 4 9 0 14c-4-5-4-11 0-14z"/></svg>Organic</div>
    <div><svg width="34" height="34" viewBox="0 0 34 34" fill="none" stroke="#333" stroke-width="1.3"><circle cx="17" cy="17" r="13"/><path d="M8 8l18 18"/><path d="M13 10h8M15 10v6l-4 8h12l-4-8v-6"/></svg>No Chemicals</div>
  </div>
  <div class="btns"><span class="btn btn-outline" style="width:98px">Read More</span><span class="btn btn-green" style="width:98px">Shop Now</span></div>
</section>

<div class="abs band-grey" style="top:1221px;height:601px"></div>
<div class="sec-title" style="top:1276px"><h2>Features Products</h2></div>
<div class="tabs"><span class="on">Edibles</span><span>THCA Flower</span><span>Concentrates</span><span>Vapes</span></div>

<div class="card" style="left:91px;top:1383px;height:384px"><div class="shot" style="background:linear-gradient(160deg,#fafafa,#d9d9d9)" role="img" aria-label="Jar of THCA flower with a bud beside it"></div><span class="off">-15%</span>
  <div class="meta" style="top:300px"><div class="stars">★★★★★<em>(0)</em></div><h3>THCA Flower</h3><div class="price">$100.00<s>$124.00</s></div></div></div>
<div class="card" style="left:353px;top:1383px;height:384px"><div class="shot" style="background:linear-gradient(160deg,#fafafa,#f2e6b8)" role="img" aria-label="Open tin of golden concentrate wax"></div><span class="off">-11%</span>
  <div class="meta" style="top:300px"><div class="stars">★★★★★<em>(0)</em></div><h3>Concentrates</h3><div class="price">$160.00<s>$180.00</s></div></div></div>
<div class="card" style="left:611px;top:1383px;height:384px"><div class="shot" style="background:linear-gradient(160deg,#fafafa,#bfe9e3)" role="img" aria-label="Teal pouch of melon gummies"></div><span class="off">-8%</span>
  <div class="meta" style="top:300px"><div class="stars">★★★★★<em>(0)</em></div><h3>Edibles</h3><div class="price">$90.00<s>$98.00</s></div></div></div>
<div class="card" style="left:871px;top:1383px;height:384px"><div class="shot" style="background:linear-gradient(160deg,#fafafa,#cfcfcf)" role="img" aria-label="Black vape device with pen"></div><span class="off">-10%</span>
  <div class="meta" style="top:300px"><div class="stars">★★★★★<em>(0)</em></div><h3>Vapes</h3><div class="price">$90.00<s>$100.00</s></div></div></div>

<div class="abs promo" style="left:91px">
  <div class="txt"><small>Sale off 45%</small><b>Concentrates</b><p>Hurry, Limited Time Offer - Massive Summer Sale!</p><span class="btn btn-green">Shop Now</span></div>
  <div class="art" style="left:240px;top:30px;width:240px;height:250px;background:radial-gradient(circle at 50% 55%,#f5d84a 0%,#2b2b2b 45%,rgba(0,0,0,0) 70%)" role="img" aria-label="Tipped jar spilling yellow concentrate"></div>
</div>
<div class="abs promo" style="left:609px">
  <div class="txt"><small>Quality cannabis</small><b>Edibles</b><span class="btn btn-green">Shop Now</span></div>
  <div class="art" style="left:250px;top:20px;width:220px;height:265px;background:radial-gradient(ellipse at 50% 50%,#3a6fd1 0%,#c73434 50%,rgba(0,0,0,0) 72%)" role="img" aria-label="Bottle of berry flavour gummies with gummies around it"></div>
</div>

<div class="sec-title" style="top:2296px"><h2>Specials Deals</h2><p>Hurry Up and Take Advantage of Our Special Deals on Cannabis Oil</p></div>

<div class="card" style="left:91px;top:2374px;height:390px"><div class="shot" style="background:linear-gradient(160deg,#fafafa,#d9d9d9)" role="img" aria-label="Jar of THCA flower"></div>
  <div class="count"><span>159</span><i>:</i><span>11</span><i>:</i><span>13</span><i>:</i><span>52</span></div>
  <div class="meta" style="top:304px"><div class="stars">★★★★★<em>(0)</em></div><h3>THCA Flower</h3><div class="price">$10.00 – $40.00</div></div></div>
<div class="card" style="left:353px;top:2374px;height:390px"><div class="shot" style="background:linear-gradient(160deg,#fafafa,#f2e6b8)" role="img" aria-label="Tin of concentrate wax"></div><span class="off">-8%</span>
  <div class="count"><span>165</span><i>:</i><span>11</span><i>:</i><span>13</span><i>:</i><span>52</span></div>
  <div class="meta" style="top:304px"><div class="stars">★★★★★<em>(0)</em></div><h3>Concentrates</h3><div class="price">$110.00<s>$120.00</s></div></div></div>
<div class="card" style="left:611px;top:2374px;height:390px"><div class="shot" style="background:linear-gradient(160deg,#fafafa,#bfe9e3)" role="img" aria-label="Pouch of melon gummies"></div><span class="off">-11%</span>
  <div class="count"><span>160</span><i>:</i><span>11</span><i>:</i><span>13</span><i>:</i><span>52</span></div>
  <div class="meta" style="top:304px"><div class="stars">★★★★★<em>(0)</em></div><h3>Edibles</h3><div class="price">$160.00<s>$180.00</s></div></div></div>
<div class="card" style="left:871px;top:2374px;height:390px"><div class="shot" style="background:linear-gradient(160deg,#fafafa,#cfcfcf)" role="img" aria-label="Black vape device"></div><span class="off">-8%</span>
  <div class="count"><span>137</span><i>:</i><span>11</span><i>:</i><span>13</span><i>:</i><span>52</span></div>
  <div class="meta" style="top:304px"><div class="stars">★★★★★<em>(0)</em></div><h3>Vapes</h3><div class="price">$90.00<s>$98.00</s></div></div></div>

<div class="benefit" style="left:91px;top:2857px"><span class="ic"><svg width="30" height="30" viewBox="0 0 30 30" fill="none" stroke="#fff" stroke-width="1.5"><circle cx="15" cy="15" r="10"/><path d="M15 5v20M9 10c3 2 3 8 0 10M21 10c-3 2-3 8 0 10"/></svg></span><div><h4>Nervous system impact</h4><p>Cannabis essential oil has a notable impact on the nervous system. It can promote relaxation, reduce stress.</p></div></div>
<div class="benefit" style="left:433px;top:2857px"><span class="ic"><svg width="30" height="30" viewBox="0 0 30 30" fill="none" stroke="#fff" stroke-width="1.5"><circle cx="15" cy="15" r="7"/><path d="M5 8v14M25 8v14M3 8v5h4V8"/></svg></span><div><h4>Appetite stimulation</h4><p>Cannabis essential oil stimulates appetite, aiding individuals with reduced hunger due to medical conditions or treatments.</p></div></div>
<div class="benefit" style="left:91px;top:2962px"><span class="ic"><svg width="30" height="30" viewBox="0 0 30 30" fill="none" stroke="#fff" stroke-width="1.5"><circle cx="15" cy="15" r="10"/><circle cx="15" cy="15" r="6"/><circle cx="15" cy="15" r="2"/></svg></span><div><h4>Pain relief</h4><p>It's relieves pain by providing analgesic, making it effective for managing discomfort associated with various conditions.</p></div></div>
<div class="benefit" style="left:433px;top:2962px"><span class="ic"><svg width="30" height="30" viewBox="0 0 30 30" fill="none" stroke="#fff" stroke-width="1.5"><path d="M15 4l9 4v7c0 6-4 9-9 11c-5-2-9-5-9-11V8z"/><path d="M11 15l3 3 5-6"/></svg></span><div><h4>Antioxidant</h4><p>Cannabis essential oil is rich in antioxidants, which help protect cells from damage caused by free radicals.</p></div></div>
<div class="benefit" style="left:91px;top:3067px"><span class="ic"><svg width="30" height="30" viewBox="0 0 30 30" fill="none" stroke="#fff" stroke-width="1.5"><rect x="6" y="6" width="18" height="18" rx="3"/><path d="M10 13h3M17 13h3M11 19c2 2 6 2 8 0"/></svg></span><div><h4>Sleep aid</h4><p>It is known for its potential as a sleep aid. It can help promote relaxation, induce a sense of calmness, improve sleep quality.</p></div></div>
<div class="benefit" style="left:433px;top:3067px"><span class="ic"><svg width="30" height="30" viewBox="0 0 30 30" fill="none" stroke="#fff" stroke-width="1.5"><rect x="5" y="11" width="20" height="8" rx="4" transform="rotate(-35 15 15)"/><path d="M12 10l6 9"/></svg></span><div><h4>Holistic Pharmacy</h4><p>These pharmacies offer a variety of Cannabis essential oil products, such as oils, capsules, and topicals.</p></div></div>
<div class="abs video ph" role="img" aria-label="Gloved hand handling cannabis plants in a grow room"><span class="play"></span><svg class="abs" style="left:160px;top:135px" width="14" height="16" viewBox="0 0 14 16"><path d="M1 1l12 7-12 7z" fill="#fff"/></svg></div>

<div class="abs band-grey ship-band"></div>
<div class="abs van" role="img" aria-label="Branded black and white delivery van"></div>
<div class="svc" style="left:106px;top:3318px"><h4><svg width="16" height="12" viewBox="0 0 16 12" fill="none" stroke="#333"><rect x="1" y="2" width="9" height="7"/><path d="M10 4h3l2 3v2h-5"/></svg>Free Shipping</h4><p>Weed websites may provide free shipping,<br>meaning no extra charges for delivery.</p></div>
<div class="svc" style="left:864px;top:3318px"><h4><svg width="14" height="14" viewBox="0 0 14 14" fill="none" stroke="#333"><path d="M7 1l6 3v6l-6 3-6-3V4z"/></svg>Discreet Packaging</h4><p>Weed websites use discreet packaging to maintain<br>privacy and confidentiality.</p></div>
<div class="svc" style="left:80px;top:3410px"><h4><svg width="14" height="14" viewBox="0 0 14 14" fill="none" stroke="#333"><path d="M3 7a4 4 0 1 0 2-3.5M3 1v3h3"/></svg>Return Policy</h4><p>Return policies vary for weed websites. Check the<br>website for their specific return policy.</p></div>
<div class="svc" style="left:864px;top:3410px"><h4><svg width="14" height="14" viewBox="0 0 14 14" fill="none" stroke="#333"><rect x="1" y="3" width="12" height="8"/><circle cx="7" cy="7" r="2"/></svg>Money Back Guarantee</h4><p>Websites prioritize payment security to protect<br>customer of a information transactions.</p></div>

<div class="sec-title" style="top:3642px"><h2>Latest News</h2><p>Unveiling the Mysteries of Cannabis Essential Oil and Its Versatile Applications</p></div>
<div class="abs news-main ph" role="img" aria-label="Hand holding a glass bowl of capsules among cannabis leaves"></div>
<article class="abs news-body">
  <div class="date">06TH FEB 2025</div>
  <h3>Dosage and Safety Considerations</h3>
  <p>Harnessing the Potential of Cannabis Oil for Wellness Empowering Wellness with the Healing Properties of Cannabis Oil Shop Now Learn more The Promising Role of Cannabis in Healthcare From health to culinary pleasure, explore the limitless applications of cannabis essential oil Shop Now Learn more Exploring medicinal properties and wellness applications. Empowering Wellness with the Healing Properties of Cannabis Oil Shop Now...</p>
  <span class="more">Read More →</span>
</article>
<article class="news-item" style="top:3723px"><div class="thumb" style="background:linear-gradient(160deg,#e8eef0,#4c7a4a)" role="img" aria-label="Dropper bottle beside a cannabis leaf"></div>
  <div class="body"><h3 style="margin-top:4px">Cannabis and Mental Health</h3><p>Duis commodo faucibus lectus, at accumsan quam egestas et. Praesent eros mi, condimentum sit amet felis quis, hendrerit ullamcorper turpis vehicula nibh mauris, gravida odio in sem laoreet...</p><span class="more">Read More →</span></div></article>
<article class="news-item" style="top:3896px"><div class="thumb" style="background:linear-gradient(160deg,#3b5a3a,#8faac0)" role="img" aria-label="Gloved hand trimming a cannabis plant"></div>
  <div class="body"><div class="date">01ST FEB 2025</div><h3>Power from Plants</h3><p>Duis commodo faucibus lectus, at accumsan quam egestas et. Praesent eros mi, condimentum sit amet felis quis, hendrerit ullamcorper turpis vehicula nibh mauris, gravida odio in sem laoreet...</p><span class="more">Read More →</span></div></article>
<article class="news-item" style="top:4069px"><div class="thumb" style="background:linear-gradient(160deg,#2d4a2a,#5f7d3f)" role="img" aria-label="Scissors trimming cannabis leaves"></div>
  <div class="body"><div class="date">01ST JAN 2025</div><h3>Nature's Calm Gift</h3><p>Duis commodo faucibus lectus, at accumsan quam egestas et. Praesent eros mi, condimentum sit amet felis quis, hendrerit ullamcorper turpis vehicula nibh mauris, gravida odio in sem laoreet...</p><span class="more">Read More →</span></div></article>
<div class="abs scroll"><i></i></div>

<div class="abs band-grey" style="top:4314px;height:424px"></div>
<div class="sec-title" style="top:4356px"><h2>Customer Reviews</h2><p>How Cannabis Oil Has Made a Difference for Our Customers</p></div>
<div class="review" style="left:91px"><div class="avatar" style="background:linear-gradient(160deg,#3a2a2a,#b07a5a)" role="img" aria-label="Customer portrait"></div>
  <div class="who"><b>Marco Reyes</b><small>Wellness Coaches</small><span class="st">★★★★★</span></div>
  <span class="q">“</span><p>I've found Fernvale Cannabis Essential Oil to be a great addition to my skincare routine. It has a soothing effect on my skin and helps reduce redness and inflammation.</p></div>
<div class="review" style="left:436px"><div class="avatar" style="background:linear-gradient(160deg,#5a2a2a,#c46a5a)" role="img" aria-label="Customer portrait"></div>
  <div class="who"><b>Dana Holt</b><small>Holistic Practitioners</small><span class="st">★★★★★</span></div>
  <span class="q">“</span><p>I appreciate that Fernvale Cannabis Essential Oil is 100% pure therapeutic grade. It gives me peace of mind knowing that I'm using a high-quality product.</p></div>
<div class="review" style="left:782px"><div class="avatar" style="background:linear-gradient(160deg,#2a3a5a,#8a8aa0)" role="img" aria-label="Customer portrait"></div>
  <div class="who"><b>Owen Pierce</b><small>Skincare Professionals</small><span class="st">★★★★★</span></div>
  <span class="q">“</span><p>I use this oil in my diffuser, and it creates a wonderfully calming atmosphere in my home. The earthy aroma is very pleasant and helps me unwind after a long day.</p></div>

<div class="abs foot-brand"><span class="brand-mark"></span><span class="brand-name" style="font-size:14px;width:80px">Ridgeline Hemp</span></div>
<div class="abs foot-contact">
  <div><svg width="8" height="10" viewBox="0 0 8 10"><path d="M4 0a4 4 0 0 1 4 4c0 3-4 6-4 6S0 7 0 4a4 4 0 0 1 4-4z" fill="#222"/></svg>120 Cedar Hollow Lane, Fairview, TX 75001</div>
  <div><svg width="9" height="9" viewBox="0 0 9 9"><path d="M1 0h2l1 2-1 1c1 2 2 3 3 3l1-1 2 1v2c-5 0-9-4-8-8z" fill="#222"/></svg>+1 555 0134 220</div>
  <div><svg width="10" height="8" viewBox="0 0 10 8"><rect width="10" height="8" fill="#222"/><path d="M0 0l5 4 5-4" stroke="#fff" fill="none"/></svg>hello@ridgelinehemp.com</div>
</div>
<div class="fcol" style="left:349px"><h4>Customer Service</h4><a>Privacy Policy</a><a>Term Of Use</a><a>Delivery</a></div>
<div class="fcol" style="left:606px"><h4>Support</h4><a>FAQ's</a><a>Return</a><a>Shipping</a></div>
<div class="fcol" style="left:864px"><h4>Newsletter</h4>
  <div class="news-form"><span>Enter Your Email</span><b>Subscribe</b></div>
  <h4 style="margin-top:18px;margin-bottom:0">Follow Us</h4>
  <div class="social"><i></i><i></i><i></i><i></i></div>
</div>
<div class="abs copy">Copyright © 2025 ridgelinehemp.com, All rights reserved.</div>
<div class="abs pay"><i></i><i></i><i></i><i></i><i></i><i></i></div>

</body>
</html>
```